Bref créative
Biz Card for a Professional Organizer
Dana Kowalt
Cutting-Edge
Room Clearing Maestro
Serving the Bay Area
info@42plumova.com
www.42plumova.com
I'd like a clean design, possibly going vertical instead of the traditional horizontal-UNLESS it is just going to look better going horizontal.
I'm open to suggestions here. I also have black and white versions of my logo if that would work well here...
black version of logo
reverse version of logo
color version

```html
<!DOCTYPE html>
<html lang="en">
<head>
<meta charset="utf-8">
<title>42 Plumova Stationery Concepts</title>
<link href="https://fonts.googleapis.com/css2?family=Montserrat:wght@400;600;700&display=swap" rel="stylesheet">
<style>
:root{
  --stage:#3b2c22;
  --paper:#ffffff;
  --teal:#3f7f93;
  --brown:#6b4a35;
  --ghost:#e4ecef;
  --ink:#5a5a5a;
  --label:#cfc3b8;
}
*{margin:0;padding:0;box-sizing:border-box}
html,body{width:1200px;height:442px;overflow:hidden}
body{background:var(--stage);font-family:'Montserrat',sans-serif;position:relative}
.label{position:absolute;font-size:6px;line-height:8px;letter-spacing:.5px;text-transform:uppercase;color:var(--label);text-align:center}
.card-label{font-size:4.5px;line-height:6px;letter-spacing:.3px;width:38px}
.sheet{position:absolute;background:var(--paper);overflow:hidden;box-shadow:0 3px 8px rgba(0,0,0,.45)}
.brand{position:absolute;font-weight:700;color:var(--teal);white-space:nowrap}
.ghost-name{position:absolute;font-weight:700;color:var(--ghost);white-space:nowrap;line-height:1}
.corner{position:absolute;top:0;right:0}
.contact{position:absolute;font-size:4px;line-height:6px;color:var(--ink)}
/* cards */
.card{width:36px;height:72px;top:312px}
.card-front{left:24px}
.card-back{left:67px;background:var(--teal)}
.card-front .brand{font-size:5px;left:3px;top:6px}
.card-front .contact{left:3px;right:2px;top:44px;font-size:3px;line-height:4.5px;white-space:nowrap}
.card-back .brand{color:var(--paper);font-size:7px;line-height:8px;left:0;right:0;top:28px;text-align:center;white-space:normal}
/* letterheads */
.letterhead{width:271px;height:392px;top:29px}
.lh-one{left:221px}
.lh-two{left:509px}
.letterhead .brand{font-size:20px;left:50px;top:14px}
.letterhead .ghost-name{font-size:70px;left:50px;top:270px}
/* envelopes */
.envelope{left:816px;width:360px}
.env-teal{top:29px;height:62px;background:var(--teal)}
.env-brown{top:101px;height:79px;background:var(--brown)}
.env-white{top:187px;height:64px}
.env-large{top:266px;height:130px}
.envelope .brand{color:var(--paper);font-size:13px;left:50%;transform:translateX(-50%)}
.env-teal .brand{top:20px}
.env-brown .brand{top:30px}
.env-white .brand{color:var(--teal);top:28px}
.env-large .brand{font-size:18px;left:16px;top:14px;transform:none}
.flap{position:absolute;left:0;top:0}
</style>
</head>
<body>
<div class="label" style="left:14px;top:150px;width:90px">Stationery Concepts</div>

<section class="sheet card card-front">
  <div class="brand">42 Plumova</div>
  <div class="contact">
    Dana Kowalt<br>Room Clearing<br>Maestro<br>info@42plumova.com<br>www.42plumova.com
  </div>
</section>
<section class="sheet card card-back">
  <div class="brand">42<br>Plumova</div>
</section>
<div class="label card-label" style="left:23px;top:390px">Business Card Front</div>
<div class="label card-label" style="left:66px;top:390px">Business Card Back</div>

<section class="sheet letterhead lh-one">
  <svg class="corner" width="110" height="30" viewBox="0 0 110 30">
    <rect x="20" y="0" width="90" height="14" fill="var(--teal)"/>
    <path d="M0 0 Q60 26 110 18 L110 30 Q55 34 0 0Z" fill="var(--brown)"/>
  </svg>
  <div class="brand">42 Plumova</div>
  <div class="ghost-name">42</div>
  <div class="contact" style="left:50px;top:376px">555 214 0386 · info@42plumova.com · www.42plumova.com</div>
</section>
<div class="label" style="left:221px;top:428px;width:271px">Letterhead Option 1</div>

<section class="sheet letterhead lh-two">
  <svg class="corner" width="110" height="30" viewBox="0 0 110 30">
    <rect x="20" y="0" width="90" height="14" fill="var(--teal)"/>
    <path d="M0 0 Q60 26 110 18 L110 30 Q55 34 0 0Z" fill="var(--brown)"/>
  </svg>
  <div class="brand" style="left:100px">42 Plumova</div>
  <div class="ghost-name">42</div>
  <div class="contact" style="left:50px;top:376px">555 214 0386 · info@42plumova.com · 42_Plumova</div>
</section>
<div class="label" style="left:509px;top:428px;width:271px">Letterhead Option 2</div>

<section class="sheet envelope env-teal">
  <div class="brand">42 Plumova</div>
</section>
<section class="sheet envelope env-brown">
  <svg class="flap" width="360" height="30" viewBox="0 0 360 30"><path d="M0 0 L180 26 L360 0Z" fill="#ffffff"/></svg>
  <div class="brand">42 Plumova</div>
</section>
<section class="sheet envelope env-white">
  <svg class="flap" width="360" height="24" viewBox="0 0 360 24"><path d="M0 0 L180 20 L360 0Z" fill="var(--ghost)"/></svg>
  <div class="brand">42 Plumova</div>
</section>
<div class="label" style="left:816px;top:255px;width:360px">Envelope Options</div>

<section class="sheet envelope env-large">
  <svg class="corner" width="140" height="36" viewBox="0 0 140 36">
    <rect x="30" y="0" width="110" height="16" fill="var(--teal)"/>
    <path d="M0 0 Q80 30 140 20 L140 36 Q70 40 0 0Z" fill="var(--brown)"/>
  </svg>
  <div class="brand">42 Plumova</div>
  <div class="contact" style="left:16px;top:38px">Serving the Bay Area<br>www.42plumova.com</div>
</section>
<div class="label" style="left:816px;top:402px;width:360px">Standard Envelope</div>
</body>
</html>
```